Executive Presence Book Cover for Lantern Mentoring

I am looking for 10 book covers that are unified and work very well together. they have to be simple with an international feel.I will be using the colors of the rainbows for the color of the books and all I am looking for is a creative way to write the title of the book on the cover. The ten titles are as follows: Transparency, Humility, Poise ,Charisma ,Relationships, Results, Clarity, Being Present, Grooming and Appearance,Acumen

Target Market(s)

business executives

Font styles to use
Other font styles liked:
• use any font you think would work

Colors

Designer to choose colors to be used in the design.

Requirements
Must have
• simple, easy to read, looking for the word to be the focus/focal point of the cover. we will be putting information on the back cover of our company etc.
• only the words of the title nothing else. The size of the book is 9“ x 7“. The only thing on the outside of the book is the title, no author nothing else. We will be putting information on the back cover of the book in very simple font.
Nice to have
• i would like each title of the 10 book covers to be clean, consistent and elegant and corporate. as long as it is not too "SILLY" i would like the titles to speak of their purpose. for instance,
• charisma could have a letter that look elegant
• being present could have some bold letters.
Should not have
• alot of drawings or pictures
• they can't be jovial, light or humorous treatments.

```html
<!DOCTYPE html>
<html lang="en">
<head>
<meta charset="utf-8">
<title>Executive Presence Book Covers</title>
<link rel="stylesheet" href="https://fonts.googleapis.com/css2?family=Bebas+Neue&display=swap">
<style>
  :root {
    --page-bg: #ffffff;
    --title-ink: #141210;
    --rule-ink: #141210;
    --relationships-a: #f2a0ae; --relationships-b: #c81e3c;
    --poise-a: #f6b48c; --poise-b: #a8320e;
    --humility-a: #f3d48a; --humility-b: #2a1e04;
    --charisma-a: #c8f0b8; --charisma-b: #23451c;
    --transparency-a: #a8d4ea; --transparency-b: #1e4658;
    --present-a: #d8a8cc; --present-b: #7a3a68;
    --results-a: #d8c0ec; --results-b: #5c3a7c;
    --clarity-a: #f4e6cc; --clarity-b: #2c2218;
    --grooming-a: #e6efc6; --grooming-b: #39451c;
    --acumen-a: #f8cdeb; --acumen-b: #5a0c3c;
  }
  * { box-sizing: border-box; margin: 0; padding: 0; }
  html, body {
    width: 1200px; height: 678px; overflow: hidden;
    background: var(--page-bg);
  }
  .cover-set { position: relative; width: 1200px; height: 678px; }
  .cover {
    position: absolute; width: 210px; height: 297px; overflow: hidden;
  }
  .cover-art { position: absolute; inset: 0; }
  .cover-title {
    position: absolute; left: 50%; top: 94px; transform: translateX(-50%);
    padding: 3px 9px 1px;
    border-top: 1.5px solid var(--rule-ink);
    border-bottom: 1.5px solid var(--rule-ink);
    font-family: "Bebas Neue", "Arial Narrow", sans-serif;
    font-size: 34px; line-height: 33px; letter-spacing: 1.5px;
    color: var(--title-ink); white-space: nowrap; text-align: center;
  }
  .cover-title.two-line { top: 91px; padding: 4px 14px 2px; line-height: 30px; }

  .row-top { top: 30px; } .row-bottom { top: 349px; }
  .col-1 { left: 44px; } .col-2 { left: 268px; } .col-3 { left: 492px; }
  .col-4 { left: 717px; } .col-5 { left: 953px; }

  .relationships .cover-art { background: linear-gradient(180deg, var(--relationships-b) 0%, var(--relationships-a) 55%, var(--relationships-b) 100%); }
  .poise .cover-art { background: linear-gradient(160deg, var(--poise-a) 0%, #d9602a 45%, var(--poise-b) 100%); }
  .humility .cover-art { background: linear-gradient(180deg, #7a5a10 0%, var(--humility-a) 35%, #9c7a30 65%, var(--humility-b) 100%); }
  .charisma .cover-art { background: linear-gradient(180deg, var(--charisma-a) 0%, #9ed490 45%, var(--charisma-b) 100%); }
  .transparency .cover-art { background: linear-gradient(180deg, var(--transparency-a) 0%, #7fa8bc 50%, var(--transparency-b) 100%); }
  .being-present .cover-art { background: linear-gradient(180deg, var(--present-b) 0%, var(--present-a) 45%, var(--present-b) 100%); }
  .results .cover-art { background: linear-gradient(180deg, var(--results-b) 0%, var(--results-a) 55%, #7a5a96 100%); }
  .clarity .cover-art { background: linear-gradient(180deg, #d8ccb4 0%, var(--clarity-a) 40%, #6a5a48 75%, var(--clarity-b) 100%); }
  .grooming .cover-art { background: linear-gradient(180deg, #a8b48a 0%, var(--grooming-a) 20%, #6e7c44 50%, var(--grooming-b) 100%); }
  .acumen .cover-art { background: linear-gradient(180deg, var(--acumen-a) 0%, #e08cc4 50%, var(--acumen-b) 100%); }
</style>
</head>
<body>
<main class="cover-set">
  <section class="cover relationships row-top col-1">
    <div class="cover-art" role="img" aria-label="Red-tinted photo of a sunset over the sea with a wave on the beach"></div>
    <h2 class="cover-title">Relationships</h2>
  </section>
  <section class="cover poise row-top col-2">
    <div class="cover-art" role="img" aria-label="Orange-tinted photo of sea cliffs above a curving beach"></div>
    <h2 class="cover-title">Poise</h2>
  </section>
  <section class="cover humility row-top col-3">
    <div class="cover-art" role="img" aria-label="Golden-tinted photo of a lake framed by palm leaves"></div>
    <h2 class="cover-title">Humility</h2>
  </section>
  <section class="cover charisma row-top col-4">
    <div class="cover-art" role="img" aria-label="Green-tinted photo of a river winding through a mountain valley"></div>
    <h2 class="cover-title">Charisma</h2>
  </section>
  <section class="cover transparency row-top col-5">
    <div class="cover-art" role="img" aria-label="Blue-tinted photo of mountain peaks above a lake with pine trees"></div>
    <h2 class="cover-title">Transparency</h2>
  </section>

  <section class="cover being-present row-bottom col-1">
    <div class="cover-art" role="img" aria-label="Mauve-tinted photo of a bridge reflected in a river under a dramatic sky"></div>
    <h2 class="cover-title">Being Present</h2>
  </section>
  <section class="cover results row-bottom col-2">
    <div class="cover-art" role="img" aria-label="Purple-tinted photo of a hiker with raised arms standing on a rock"></div>
    <h2 class="cover-title">Results</h2>
  </section>
  <section class="cover clarity row-bottom col-3">
    <div class="cover-art" role="img" aria-label="Sepia-tinted photo of mountain lakes under a cloudy sky"></div>
    <h2 class="cover-title">Clarity</h2>
  </section>
  <section class="cover grooming row-bottom col-4">
    <div class="cover-art" role="img" aria-label="Olive-tinted photo of a forested hillside with rocks under a bright sky"></div>
    <h2 class="cover-title two-line">Grooming and<br>Appearance</h2>
  </section>
  <section class="cover acumen row-bottom col-5">
    <div class="cover-art" role="img" aria-label="Magenta-tinted photo of a misty forest with bare trees"></div>
    <h2 class="cover-title">Acumen</h2>
  </section>
</main>
</body>
</html>
```